Healing stone/crystal Shopify store

Hi - I'm creating a new site to sell healing crystals/stones.Name for the shop is MoonpetalHaven. Site helps people to choose best crystals for them .Shop should have blog aswell.The site should be informative and attractive. Stones we sell Opalite,Green Aventurine,Watermelon Crystal,Rose Quartz Stone,Tiger Eye Stone. Must be Shopify. No content yet, you can fill neccessary fields Lorea Ipsum and if you have some good idea you can put it there
Updates

Designs look the same

Target Market(s)

Woman, English speaking countries.

Industry/Entity Type

Shop

Number of Pages Required

1 page

Colors

Designer to choose colors to be used in the design.

Requirements
Must have
• Blog
Nice to have
• High quality pictures to look site attractive.

```html
<!DOCTYPE html>
<html lang="en">
<head>
<meta charset="utf-8">
<title>MoonpetalHaven – Healing Crystals</title>
<link href="https://fonts.googleapis.com/css2?family=Montserrat:ital,wght@0,700;1,700&family=Open+Sans:wght@400;600;700&display=swap" rel="stylesheet">
<style>
:root{
  --white:#ffffff;
  --page:#e4e4e4;
  --ink:#111111;
  --text:#333333;
  --muted:#6b6b6b;
  --line:#a8a8a8;
  --accent:#f04a25;
  --green:#1e9b2f;
  --blue:#3d68bf;
  --purple:#9a50a8;
  --dark:#3a3a3a;
  --sky:#2fa8dd;
  --steel:#62707a;
}
*{box-sizing:border-box;margin:0;padding:0}
html,body{width:768px;height:1200px;overflow:hidden}
body{position:relative;background:var(--page);font-family:"Open Sans",Arial,sans-serif;color:var(--text)}
.abs{position:absolute}
svg.icon{display:block}

.site-header{left:0;top:0;width:768px;height:66px;background:var(--white)}
.brand{left:57px;top:23px;font-family:"Montserrat",Arial,sans-serif;font-weight:700;font-size:16px;color:var(--ink)}
.social-top{left:397px;top:24px;display:flex;gap:2px}
.social-top span{width:17px;height:17px;border-radius:50%;background:var(--dark);display:flex;align-items:center;justify-content:center}
.search{left:557px;top:23px;width:151px;height:22px;border:1.5px solid var(--dark);font-size:8px;padding:5px 6px;color:#555}
.search svg{position:absolute;right:4px;top:4px}

.hero{left:0;top:66px;width:768px;height:322px;overflow:hidden;
  background:
    radial-gradient(circle at 205px 80px,rgba(255,255,255,.85) 0,rgba(255,255,255,0) 14px),
    radial-gradient(circle at 270px 40px,rgba(255,255,255,.8) 0,rgba(255,255,255,0) 10px),
    radial-gradient(circle at 150px 260px,rgba(255,255,255,.7) 0,rgba(255,255,255,0) 12px),
    radial-gradient(circle at 340px 230px,rgba(255,255,255,.7) 0,rgba(255,255,255,0) 10px),
    linear-gradient(100deg,#c9a2dc 0%,#a862c2 28%,#b97fcf 50%,#e3cdea 78%,#f4edf6 100%)}
.hero-figures{left:378px;top:120px;width:320px;height:268px;
  background:
    radial-gradient(ellipse 60px 120px at 70px 150px,#5c5644 0%,#4a4537 60%,rgba(74,69,55,0) 100%),
    radial-gradient(ellipse 60px 115px at 160px 140px,#a86e2c 0%,#7a4c20 60%,rgba(122,76,32,0) 100%),
    radial-gradient(ellipse 65px 110px at 250px 110px,#3c4c9a 0%,#26306a 60%,rgba(38,48,106,0) 100%)}
.hero-title{left:57px;top:265px;font-family:"Montserrat",Arial,sans-serif;font-style:italic;font-weight:700;font-size:18px;line-height:22px;color:var(--white);text-shadow:0 1px 3px rgba(80,30,90,.35)}

.tabs{left:76px;top:396px;font-size:9px;font-weight:700;color:var(--ink);border-bottom:1px solid var(--line);padding-bottom:3px;width:78px}
.tabs .muted{color:var(--muted);font-weight:600}
.product{width:150px}
.product-image{width:122px;height:122px;border:2px solid #b5b5b5;background:var(--white)}
.product-name,.product-price{font-size:11.5px;font-weight:600;color:#666;margin-left:7px;letter-spacing:.3px}
.product-name{margin-top:4px}
.product-price{margin-top:5px}
.product-actions{display:flex;gap:7px;margin-top:4px;margin-left:9px}
.btn{display:inline-block;color:var(--white);font-size:10px;font-weight:700;text-align:center;line-height:15px;height:15px;width:47px}
.btn-shop{background:var(--green)}
.btn-share{background:var(--blue)}
.divider{left:49px;top:633px;width:662px;height:1px;background:#9a9a9a}

.post{left:94px;width:411px;height:224px;background:var(--white)}
.post-image{position:absolute;left:21px;top:24px;width:176px;height:176px}
.post-title{position:absolute;left:205px;top:27px;color:var(--accent);font-size:12px;font-weight:400}
.post-body{position:absolute;left:206px;top:51px;width:178px;font-size:6.3px;line-height:9.6px;color:#555}
.post-body p+p{margin-top:6px}
.post-meta{position:absolute;left:206px;top:173px;width:190px;border-top:1px solid #ccc;padding-top:12px;display:flex;justify-content:space-between;font-size:4.6px;color:#555}
.post-meta span{display:flex;align-items:center;gap:2px}
.post-meta i{display:inline-block;width:6px;height:6px;background:#8a8a8a;border-radius:1px}
.share-rail{left:77px;width:17px}
.share-rail span{display:flex;align-items:center;justify-content:center;width:17px;height:17px;margin-bottom:1px}

.sidebar{left:534px;top:670px;width:177px;height:483px;background:var(--white)}
.side-title{position:absolute;left:24px;font-size:14px;font-weight:600;line-height:18px;color:#222}
.side-copy{position:absolute;left:24px;top:68px;font-size:8.4px;line-height:11px;color:#222}
.email{position:absolute;left:27px;top:109px;width:114px;height:30px;border:1px solid #333;font-size:11px;color:#999;padding:7px 10px}
.subscribe{position:absolute;left:27px;top:161px;width:60px;height:24px;background:var(--accent);color:var(--white);font-size:9px;text-align:center;line-height:24px}
.side-rule{position:absolute;left:27px;top:223px;width:128px;height:1px;background:#999}
.seller-thumb{position:absolute;left:27px;width:61px;height:61px;border:2px solid #b5b5b5;background:radial-gradient(ellipse 18px 26px at 50% 52%,#9a6cc4 0%,#b896d8 60%,#f1ebf6 100%)}
.seller-name{position:absolute;left:91px;font-size:14px;font-weight:600;color:#222}
.why{position:absolute;left:94px;width:41px;height:16px;background:var(--accent);color:var(--white);font-size:6px;text-align:center;line-height:16px}

.site-footer{left:0;top:1167px;width:768px;height:33px;background:var(--purple)}
.copyright{position:absolute;left:108px;top:12px;font-size:6px;color:#f0e0f4}
.social-bottom{position:absolute;left:545px;top:8px;display:flex;gap:7px}
.social-bottom span{width:16px;height:16px;border-radius:50%;border:1px solid #f0e0f4;display:flex;align-items:center;justify-content:center}
</style>
</head>
<body>

<svg width="0" height="0" style="position:absolute">
  <defs>
    <symbol id="i-mail" viewBox="0 0 16 16"><rect x="3" y="4.5" width="10" height="7" fill="none" stroke="currentColor" stroke-width="1.4"/><polyline points="3,4.5 8,8.5 13,4.5" fill="none" stroke="currentColor" stroke-width="1.4"/></symbol>
    <symbol id="i-heart" viewBox="0 0 16 16"><path d="M8 13 L3.2 8.2 A2.6 2.6 0 0 1 8 5 A2.6 2.6 0 0 1 12.8 8.2 Z" fill="currentColor"/></symbol>
    <symbol id="i-star" viewBox="0 0 16 16"><polygon points="8,2.5 9.6,6.3 13.5,6.6 10.5,9.1 11.4,13 8,10.9 4.6,13 5.5,9.1 2.5,6.6 6.4,6.3" fill="currentColor"/></symbol>
    <symbol id="i-chat" viewBox="0 0 16 16"><path d="M3 4 H13 V10.5 H7 L4.5 12.8 V10.5 H3 Z" fill="currentColor"/></symbol>
    <symbol id="i-share" viewBox="0 0 16 16"><circle cx="4.5" cy="8" r="1.8" fill="currentColor"/><circle cx="11.5" cy="4.3" r="1.8" fill="currentColor"/><circle cx="11.5" cy="11.7" r="1.8" fill="currentColor"/><path d="M4.5 8 L11.5 4.3 M4.5 8 L11.5 11.7" stroke="currentColor" stroke-width="1.2"/></symbol>
    <symbol id="i-link" viewBox="0 0 16 16"><rect x="2.5" y="6" width="6.5" height="4" rx="2" fill="none" stroke="currentColor" stroke-width="1.4"/><rect x="7" y="6" width="6.5" height="4" rx="2" fill="none" stroke="currentColor" stroke-width="1.4"/></symbol>
    <symbol id="i-plus" viewBox="0 0 16 16"><path d="M8 3.5 V12.5 M3.5 8 H12.5" stroke="currentColor" stroke-width="2"/></symbol>
    <symbol id="i-print" viewBox="0 0 16 16"><rect x="5" y="3" width="6" height="3" fill="currentColor"/><rect x="3" y="6.5" width="10" height="4.5" fill="currentColor"/><rect x="5" y="9.5" width="6" height="3.5" fill="none" stroke="currentColor" stroke-width="1.2"/></symbol>
  </defs>
</svg>

<header class="abs site-header">
  <div class="abs brand">MoonpetalHaven</div>
  <div class="abs social-top" aria-label="Social links" style="color:#fff">
    <span><svg class="icon" width="11" height="11"><use href="#i-mail"/></svg></span>
    <span><svg class="icon" width="11" height="11"><use href="#i-heart"/></svg></span>
    <span><svg class="icon" width="11" height="11"><use href="#i-star"/></svg></span>
    <span><svg class="icon" width="11" height="11"><use href="#i-chat"/></svg></span>
    <span><svg class="icon" width="11" height="11"><use href="#i-share"/></svg></span>
    <span><svg class="icon" width="11" height="11"><use href="#i-link"/></svg></span>
    <span><svg class="icon" width="11" height="11"><use href="#i-plus"/></svg></span>
  </div>
  <div class="abs search">Search
    <svg width="12" height="12" viewBox="0 0 12 12"><circle cx="5" cy="5" r="3.6" fill="none" stroke="#222" stroke-width="1.6"/><line x1="7.6" y1="7.6" x2="11" y2="11" stroke="#222" stroke-width="1.8"/></svg>
  </div>
</header>

<section class="abs hero" role="img" aria-label="Purple sparkling backdrop with glowing lights"></section>
<div class="abs hero-figures" role="img" aria-label="Three carved angel stones in pyrite, tiger eye and sodalite"></div>
<h1 class="abs hero-title">Glamorous Crystals to Heal You...<br>Only at MoonpetalHaven</h1>

<nav class="abs tabs"><span class="muted">SHOP</span> &nbsp;&nbsp;|&nbsp;&nbsp; BLOG</nav>

<div class="abs product" style="left:80px;top:426px">
  <div class="product-image" role="img" aria-label="Carved watermelon crystal elephants" style="background:radial-gradient(ellipse 62px 32px at 50% 55%,#e0505e 0%,#ef8e98 55%,#fff 100%)"></div>
  <div class="product-name">Product 1</div><div class="product-price">Price : $100</div>
  <div class="product-actions"><span class="btn btn-shop">Shop</span><span class="btn btn-share">Share</span></div>
</div>
<div class="abs product" style="left:239px;top:426px">
  <div class="product-image" role="img" aria-label="Wire tree of life pendant with blue stone chips" style="background:radial-gradient(circle at 50% 45%,#4a6fbf 0%,#8aa2d6 35%,#dfe4ee 60%,#fff 72%)"></div>
  <div class="product-name">Product 2</div><div class="product-price">Price : $50</div>
  <div class="product-actions"><span class="btn btn-shop">Shop</span><span class="btn btn-share">Share</span></div>
</div>
<div class="abs product" style="left:398px;top:426px">
  <div class="product-image" role="img" aria-label="Three small tiger eye angel figures" style="background:radial-gradient(ellipse 66px 40px at 50% 60%,#8a5424 0%,#b27a38 50%,#fff 100%)"></div>
  <div class="product-name">Product 3</div><div class="product-price">Price : $40</div>
  <div class="product-actions"><span class="btn btn-shop">Shop</span><span class="btn btn-share">Share</span></div>
</div>
<div class="abs product" style="left:558px;top:426px">
  <div class="product-image" role="img" aria-label="Pyrite angel figure" style="background:radial-gradient(ellipse 40px 60px at 50% 50%,#3a3628 0%,#625c48 55%,#fff 100%)"></div>
  <div class="product-name">Product 4</div><div class="product-price">Price : $80</div>
  <div class="product-actions"><span class="btn btn-shop">Shop</span><span class="btn btn-share">Share</span></div>
</div>

<div class="abs divider"></div>

<div class="abs share-rail" style="top:695px;color:#fff" aria-label="Share options">
  <span style="background:var(--sky)"><svg class="icon" width="12" height="12"><use href="#i-share"/></svg></span>
  <span style="background:#555"><svg class="icon" width="12" height="12"><use href="#i-chat"/></svg></span>
  <span style="background:var(--blue)"><svg class="icon" width="12" height="12"><use href="#i-heart"/></svg></span>
  <span style="background:var(--steel)"><svg class="icon" width="12" height="12"><use href="#i-mail"/></svg></span>
  <span style="background:var(--steel)"><svg class="icon" width="12" height="12"><use href="#i-print"/></svg></span>
  <span style="background:var(--accent)"><svg class="icon" width="12" height="12"><use href="#i-plus"/></svg></span>
</div>
<article class="abs post" style="top:670px">
  <div class="post-image" role="img" aria-label="Circle of carved angels in tiger eye, quartz, opalite, aventurine and rose quartz" style="background:radial-gradient(circle at 50% 48%,#2e2e2e 0%,#3a3a3a 26%,#b08a5a 40%,#e6e6ee 52%,#a8c8ea 60%,#9cc4a4 68%,#e8b6c4 76%,#3a3a3a 90%)"></div>
  <h2 class="post-title">Lorem Ipsum is simply</h2>
  <div class="post-body">
    <p>Lorem ipsum dolor sit amet, consectetur adipisicing elit, sed do eiusmod tempor incididunt ut labore et dolore magna aliqua. Ut enim ad minim veniam, quis nostrud eiusmod tempor incididunt ut labore et dolore magna aliqua exercitation ullamco laboris nisi ut aliquip ex ea commodo consequat.</p>
    <p>Ut enim ad minim veniam, quis nostrud eiusmod tempor incididunt ut labore et dolore magna aliqua exercitation ullamco laboris nisi ut aliquip ex ea commodo consequat.</p>
  </div>
  <div class="post-meta"><span><i></i>Admin</span><span><i></i>30-12-2015</span><span><i></i>3 Comments</span><span><i></i>5 favourites</span><span><i></i>1,128 views</span></div>
</article>

<div class="abs share-rail" style="top:955px;color:#fff" aria-label="Share options">
  <span style="background:var(--sky)"><svg class="icon" width="12" height="12"><use href="#i-share"/></svg></span>
  <span style="background:#555"><svg class="icon" width="12" height="12"><use href="#i-chat"/></svg></span>
  <span style="background:var(--blue)"><svg class="icon" width="12" height="12"><use href="#i-heart"/></svg></span>
  <span style="background:var(--steel)"><svg class="icon" width="12" height="12"><use href="#i-mail"/></svg></span>
  <span style="background:var(--steel)"><svg class="icon" width="12" height="12"><use href="#i-print"/></svg></span>
  <span style="background:var(--accent)"><svg class="icon" width="12" height="12"><use href="#i-plus"/></svg></span>
</div>
<article class="abs post" style="top:930px">
  <div class="post-image" role="img" aria-label="Two carved tiger eye elephants on a pale grey background" style="background:radial-gradient(ellipse 70px 34px at 50% 58%,#4a3220 0%,#7a5430 55%,#dcdcdc 100%)"></div>
  <h2 class="post-title">Lorem Ipsum is simply</h2>
  <div class="post-body">
    <p>Lorem ipsum dolor sit amet, consectetur adipisicing elit, sed do eiusmod tempor incididunt ut labore et dolore magna aliqua. Ut enim ad minim veniam, quis nostrud eiusmod tempor incididunt ut labore et dolore magna aliqua exercitation ullamco laboris nisi ut aliquip ex ea commodo consequat.</p>
    <p>Ut enim ad minim veniam, quis nostrud eiusmod tempor incididunt ut labore et dolore magna aliqua exercitation ullamco laboris nisi ut aliquip ex ea commodo consequat.</p>
  </div>
  <div class="post-meta"><span><i></i>Admin</span><span><i></i>30-12-2015</span><span><i></i>3 Comments</span><span><i></i>5 favourites</span><span><i></i>1,128 views</span></div>
</article>

<aside class="abs sidebar">
  <h3 class="side-title" style="top:17px">Sign up to our<br>newsletter</h3>
  <p class="side-copy">Pellentesque dui, non felis.<br>Maecenas male</p>
  <div class="email">Email</div>
  <div class="subscribe">Subscribe</div>
  <div class="side-rule"></div>
  <h3 class="side-title" style="top:243px">Top sellers of the<br>week</h3>
  <div class="seller-thumb" style="top:301px" role="img" aria-label="Amethyst angel figure"></div>
  <div class="seller-name" style="top:304px">Crystal 1</div>
  <div class="why" style="top:334px">Why?</div>
  <div class="seller-thumb" style="top:409px" role="img" aria-label="Amethyst angel figure"></div>
  <div class="seller-name" style="top:412px">Crystal 2</div>
  <div class="why" style="top:443px">Why?</div>
</aside>

<footer class="abs site-footer">
  <p class="copyright">© Copyrights by MoonpetalHaven 2018. All Rights Reserved.</p>
  <div class="social-bottom" aria-label="Social links" style="color:#f0e0f4">
    <span><svg class="icon" width="10" height="10"><use href="#i-mail"/></svg></span>
    <span><svg class="icon" width="10" height="10"><use href="#i-heart"/></svg></span>
    <span><svg class="icon" width="10" height="10"><use href="#i-star"/></svg></span>
    <span><svg class="icon" width="10" height="10"><use href="#i-chat"/></svg></span>
    <span><svg class="icon" width="10" height="10"><use href="#i-share"/></svg></span>
  </div>
</footer>

</body>
</html>
```